Box Design for Flooring product

***IMPORTANT: PLEASE READ THE DOCUMENT PROVIDED WITH THIS BRIEF CAREFULLY BEFORE ACCEPTING THIS PROJECT***
Need a creative design for the packaging of a flooring product. The packaging is two boxes: one holding 36 planks of flooring, and the other 7 planks of flooring. There are 4 colours for the flooring planks that need a box designed (for both the 36 plank box and 7 plank box). The boxes measures 92 cm x 16cm x 7cm (36 planks) and 92 cm x 16cm x 1.5cm (7 planks).
More details are provided in the requirements document attached with this brief. Also attaching other supporting documents with this brief mentioned in the document.
Need extra days to review
- Montserrat-Regular

```html
<!DOCTYPE html>
<html lang="en">
<head>
<meta charset="UTF-8">
<title>Veloria Flooring Box – 7 Plank Pack</title>
<link href="https://fonts.googleapis.com/css2?family=Montserrat:ital,wght@0,400;0,500;0,600;1,400&display=swap" rel="stylesheet">
<style>
  :root{
    --bg:#f3f3f3;
    --panel-dark:#2b2b2b;
    --panel-darker:#222222;
    --wood-light:#bcbcbc;
    --wood-mid:#a7a7a7;
    --ink-light:#e6e6e6;
    --ink-muted:#bdbdbd;
    --ink-dark:#2a2a2a;
    --eco:#3f7a4a;
    --rule:#6a6a6a;
  }
  *{margin:0;padding:0;box-sizing:border-box}
  html,body{width:1200px;height:1200px;overflow:hidden;background:var(--bg);font-family:"Montserrat",sans-serif}
  .canvas{position:relative;width:1200px;height:1200px}

  .box-top{position:absolute;left:50px;top:440px;width:1100px;height:190px;display:flex;overflow:hidden}
  .box-side{position:absolute;left:50px;top:630px;width:1100px;height:44px;background:var(--panel-darker);display:flex;align-items:center;padding-left:40px;gap:14px}

  .wood-panel{position:relative;width:440px;height:100%;background:linear-gradient(100deg,var(--wood-mid),var(--wood-light) 55%,var(--wood-mid))}
  .eco-badge{position:absolute;left:28px;top:22px;width:74px;height:74px;border-radius:50%;border:3px solid var(--eco);background:rgba(255,255,255,.35)}
  .wood-claims{position:absolute;left:118px;top:62px;list-style:none;color:var(--ink-dark);font-size:17px;font-weight:500;line-height:1.55}
  .wood-claims li::before{content:"•";margin-right:8px}

  .dark-panel{width:560px;height:100%;background:var(--panel-dark);display:flex;align-items:center;padding:0 18px 0 26px}
  .brand{width:200px;display:flex;align-items:center;gap:10px}
  .brand-square{width:16px;height:16px;background:var(--ink-light);flex:none}
  .brand-name{color:var(--ink-light);font-size:30px;font-weight:400;letter-spacing:2px;line-height:1}
  .brand-tag{color:var(--ink-muted);font-size:8.5px;letter-spacing:2.2px;margin-top:6px}
  .rule{width:1px;height:120px;background:var(--rule);margin:0 16px}
  .features{list-style:none;color:var(--ink-light);font-size:11px;font-style:italic;line-height:1.75;width:170px}
  .features li::before{content:"•";margin-right:6px;font-style:normal}
  .specs{display:flex;flex-direction:column;gap:10px}
  .spec{display:flex;align-items:center;gap:8px;color:var(--ink-light);font-size:9px;line-height:1.3}
  .spec svg{flex:none}

  .end-panel{width:100px;height:100%;background:linear-gradient(180deg,var(--wood-light),var(--wood-mid));display:flex;flex-direction:column;justify-content:space-around;align-items:center;padding:8px 0}
  .icon-badge{width:50px;height:50px;border-radius:50%;background:var(--panel-darker);display:flex;flex-direction:column;align-items:center;justify-content:center;color:var(--ink-light);font-size:6px;text-align:center;gap:2px}

  .side-name{color:var(--ink-light);font-size:20px;letter-spacing:2px}
  .side-tag{color:var(--ink-muted);font-size:7px;letter-spacing:2px}
</style>
</head>
<body>
<main class="canvas">
  <section class="box-top">
    <div class="wood-panel" role="img" aria-label="Grey wood plank flooring texture">
      <div class="eco-badge" role="img" aria-label="Eco-friendly certification badge"></div>
      <ul class="wood-claims">
        <li>Ideal For Bathrooms And Kitchens</li>
        <li>Suitable For General Domestic Use</li>
      </ul>
    </div>

    <div class="dark-panel">
      <div class="brand">
        <span class="brand-square"></span>
        <div>
          <div class="brand-name">VELORIA</div>
          <div class="brand-tag">PREMIUM FLOORS AND TILES</div>
        </div>
      </div>
      <span class="rule"></span>
      <ul class="features">
        <li>Easy to lay</li>
        <li>Water resistant, easy to clean</li>
        <li>Ideal for Bathrooms and Kitchens</li>
        <li>Suitable for general domestic use</li>
      </ul>
      <span class="rule"></span>
      <div class="specs">
        <div class="spec">
          <svg width="26" height="16" viewBox="0 0 26 16"><path d="M2 10 L12 4 L24 6 L14 12 Z" fill="#d9d9d9"/><path d="M2 10 L14 12 L14 14 L2 12Z" fill="#9a9a9a"/></svg>
          <span>Pack Size<br>7 Planks / 1m²</span>
        </div>
        <div class="spec">
          <svg width="26" height="16" viewBox="0 0 26 16"><rect x="2" y="3" width="22" height="10" fill="none" stroke="#d9d9d9" stroke-width="1.5"/></svg>
          <span>914 x 152mm<br>(36" x 6" approx.)</span>
        </div>
        <div class="spec">
          <svg width="26" height="16" viewBox="0 0 26 16"><path d="M2 12 L24 4 L24 7 L2 14Z" fill="#d9d9d9"/></svg>
          <span>Thickness<br>1.8mm</span>
        </div>
      </div>
    </div>

    <div class="end-panel">
      <div class="icon-badge">
        <svg width="14" height="14" viewBox="0 0 14 14"><path d="M7 1 C4 6 3 8 3 9.5 A4 4 0 0 0 11 9.5 C11 8 10 6 7 1Z" fill="#e6e6e6"/></svg>
        <span>Water Resistant</span>
      </div>
      <div class="icon-badge">
        <svg width="14" height="14" viewBox="0 0 14 14"><path d="M2 7 L6 11 L12 3" fill="none" stroke="#e6e6e6" stroke-width="2"/></svg>
        <span>Easy Clean</span>
      </div>
      <div class="icon-badge">
        <svg width="14" height="14" viewBox="0 0 14 14"><rect x="2" y="4" width="10" height="6" fill="none" stroke="#e6e6e6" stroke-width="1.5"/></svg>
        <span>Click Fit</span>
      </div>
    </div>
  </section>

  <section class="box-side">
    <span class="brand-square"></span>
    <div>
      <div class="side-name">VELORIA</div>
      <div class="side-tag">PREMIUM FLOORS AND TILES</div>
    </div>
  </section>
</main>
</body>
</html>
```